Velvet Afterhours Poster Design

Need poster design made up in next few days, can guarantee payment to winner. Poster must contain the following but feel free to word it better:
Velvet Afterhours
Presented by quendor Sounds
Select resident djs
Drink specials all night
Open from 8pm to 12pm
Find us on Linkwall
At Marlow Suites every Saturday
These will be on posters and fliers
Of a3 and roughly a5 size.
Our target audience is people 18-25
We want the posters to be exciting and professional. We would like a blue or purple with black color scheme but there is plenty of room for creative license so have a play around with what you think looks good. We currently don't have a logo but if your including one we would like to see it as c6 as in carbon as an element. Our first drink special is cocktails in jars but is not essential to include, can provide proper copy of the picture if you want to include it in your design. Please contact us if you need more information. we will be quick to pick a winner so payment will be provided fast!!!
Thank you all in advance for your submissions!!

```html
<!DOCTYPE html>
<html lang="en">
<head>
<meta charset="utf-8">
<title>Velvet Afterhours Poster</title>
<link href="https://fonts.googleapis.com/css2?family=Orbitron:wght@500;700;900&family=Yellowtail&display=swap" rel="stylesheet">
<style>
  :root {
    --night: #07050f;
    --violet: #8a3cff;
    --magenta: #c23cff;
    --blue: #2f4dff;
    --lavender: #d9c6ff;
    --white: #ffffff;
    --social: #3b5fb8;
  }
  html, body {
    margin: 0;
    padding: 0;
    overflow: hidden;
    background: var(--night);
  }
  .poster {
    position: relative;
    width: 849px;
    height: 1200px;
    overflow: hidden;
    background: var(--night);
    font-family: "Orbitron", sans-serif;
    color: var(--white);
    text-align: center;
  }
  .club-scene {
    position: absolute;
    inset: 0;
    background:
      radial-gradient(ellipse 45% 30% at 70% 22%, rgba(194,60,255,0.55), transparent 70%),
      radial-gradient(ellipse 40% 28% at 20% 30%, rgba(47,77,255,0.45), transparent 70%),
      radial-gradient(ellipse 50% 25% at 55% 55%, rgba(138,60,255,0.35), transparent 70%),
      radial-gradient(ellipse 60% 22% at 30% 92%, rgba(60,50,120,0.5), transparent 70%),
      linear-gradient(180deg, #140a2a 0%, #0c0820 45%, #06040d 75%, #0a0818 100%);
  }
  .title-band {
    position: absolute;
    inset: 0;
  }
  .headline {
    position: absolute;
    top: 170px;
    left: 0;
    width: 100%;
    margin: 0;
  }
  .headline-word {
    display: block;
    font-weight: 900;
    font-size: 104px;
    letter-spacing: 4px;
    line-height: 1;
    color: var(--white);
    -webkit-text-stroke: 4px var(--violet);
    paint-order: stroke fill;
    text-shadow: 0 0 18px rgba(194,60,255,0.8);
  }
  .headline-script {
    display: block;
    margin-top: -4px;
    font-family: "Yellowtail", cursive;
    font-weight: 400;
    font-size: 150px;
    line-height: 1.05;
    color: var(--white);
    text-shadow: 0 0 16px rgba(138,60,255,0.9), 0 0 4px var(--violet);
  }
  .presenter {
    position: absolute;
    top: 510px;
    width: 100%;
    font-size: 20px;
    font-weight: 700;
    letter-spacing: 1px;
    text-transform: uppercase;
    color: var(--white);
  }
  .line {
    position: absolute;
    width: 100%;
    font-weight: 500;
    text-transform: uppercase;
    letter-spacing: 2px;
    line-height: 1.1;
    color: var(--white);
    text-shadow: 0 0 10px rgba(138,60,255,0.9);
  }
  .features { top: 548px; font-size: 38px; color: var(--lavender); }
  .hours { top: 722px; font-size: 50px; }
  .venue { top: 935px; font-size: 40px; }
  .social {
    position: absolute;
    right: 24px;
    bottom: 22px;
    display: flex;
    align-items: center;
    gap: 10px;
    font-size: 18px;
    font-weight: 700;
    color: var(--white);
  }
  .social-square {
    width: 40px;
    height: 40px;
    background: var(--social);
  }
</style>
</head>
<body>
<main class="poster">
  <div class="club-scene" role="img" aria-label="Nightclub crowd and DJ under purple and blue lights"></div>
  <svg class="title-band" width="849" height="1200" viewBox="0 0 849 1200" aria-hidden="true">
    <polygon points="0,120 849,30 849,470 0,560" fill="#05030c" opacity="0.45"/>
    <polygon points="0,560 849,470 849,478 0,568" fill="#8a3cff" opacity="0.35"/>
  </svg>
  <h1 class="headline">
    <span class="headline-word">VELVET</span>
    <span class="headline-script">Afterhours</span>
  </h1>
  <p class="presenter" style="margin:0">Presented by quendor Sounds</p>
  <p class="line features" style="margin:0">Select resident DJs<br>Drink specials all night</p>
  <p class="line hours" style="margin:0">Open from<br>8pm to 12pm</p>
  <p class="line venue" style="margin:0">At Marlow Suites<br>every Saturday</p>
  <div class="social"><span>Linkwall</span><span class="social-square"></span></div>
</main>
</body>
</html>
```